luxury contemporary fashion website needs simple, elegant flowchart to describe the buying and selli

* Luxury, resale, preloved items are sold on this online platform
*Horizontal, simple, flowchart with 5 steps in 'friendly' font with a simple emoticon/ picture for each step
*To be positioned in the 'How we work' tab of the webpage to explain in a very simple manner the buying and selling process for the customers.
*Attached is a very rudimentary mock-up of what we would like included and an idea of a project similar to what we desire
* to confirm the text for each step, we have also attached a word file below

Industry/Entity Type

Fashion

Font styles to use
Sans Serif

Colors
86cfc6
cfeae6

Requirements
Must have
• Simple drawing / shape after each point In the closest to 'duck egg blue' fill colour you can find with a black outline

```html
<!DOCTYPE html>
<html lang="en">
<head>
<meta charset="utf-8">
<title>Bespoke Concierge Service</title>
<link href="https://fonts.googleapis.com/css2?family=Tinos:wght@400;700&display=swap" rel="stylesheet">
<style>
  :root {
    --teal: #86cfc6;
    --teal-pale: #cfeae6;
    --ink: #1a1a1a;
    --white: #ffffff;
  }
  * { box-sizing: border-box; margin: 0; padding: 0; }
  html, body { width: 1200px; height: 444px; overflow: hidden; background: var(--white); }
  body { font-family: "Tinos", "Times New Roman", serif; color: var(--ink); position: relative; }

  .title-band {
    position: absolute; left: 0; top: 18px; width: 1200px; height: 82px;
    background: var(--teal);
    display: flex; align-items: center; justify-content: center;
  }
  .title-band h1 { font-weight: 400; font-size: 51px; color: var(--white); letter-spacing: 0.3px; }

  .step {
    position: absolute; top: 148px; width: 220px; height: 180px; margin-left: -110px;
    text-align: center;
  }
  .step-badge { display: block; margin: 0 auto; width: 60px; height: 60px; }
  .step-title {
    display: inline-block; margin-top: 10px; padding: 0 0 5px;
    width: 180px; border-bottom: 1px solid var(--ink);
    font-weight: 400; font-size: 16.5px; letter-spacing: 0.2px; white-space: nowrap;
  }
  .step-text { margin-top: 9px; font-size: 13px; line-height: 1.1; }
  .step-icon { position: absolute; top: 150px; left: 50%; margin-left: -13px; width: 26px; height: 26px; }

  .payment-options {
    position: absolute; top: 253px; left: 953px; width: 220px; height: 70px;
    display: flex;
  }
  .payment-option { position: relative; width: 109px; text-align: center; font-size: 13px; line-height: 1.1; }
  .payment-divider { width: 1px; height: 68px; background: var(--ink); }
  .currency {
    position: absolute; top: 46px; left: 0; width: 100%;
    font-family: "Arial", sans-serif; font-weight: 700; font-size: 21px; color: var(--teal); letter-spacing: 0.5px;
  }
  .halo-icon { position: absolute; top: 40px; left: 50%; margin-left: -13px; width: 26px; height: 30px; }

  .action-band {
    position: absolute; left: 0; top: 363px; width: 1200px; height: 81px;
    background: var(--teal-pale);
  }
  .cta {
    position: absolute; left: 461px; top: 23px; width: 273px; height: 43px;
    background: var(--teal); color: var(--white); text-decoration: none;
    display: flex; align-items: center; justify-content: center; gap: 28px;
    font-size: 18px; letter-spacing: 0.3px;
  }
  .cta svg { width: 8px; height: 10px; }
</style>
</head>
<body>
  <header class="title-band"><h1>Bespoke Concierge Service</h1></header>

  <section class="step" style="left:128px">
    <svg class="step-badge" viewBox="0 0 60 60"><circle cx="30" cy="30" r="27" fill="none" stroke="var(--teal)" stroke-width="4"/><circle cx="30" cy="30" r="21" fill="var(--teal)"/><text x="30" y="37" text-anchor="middle" font-family="Tinos, serif" font-size="20" fill="#fff">1</text></svg>
    <h2 class="step-title">HAVE ITEMS TO SELL?</h2>
    <p class="step-text">Brandsparkling or nearly new.</p>
    <svg class="step-icon" viewBox="0 0 26 26" fill="var(--teal)"><polygon points="9,10 11,15 16,15 12,18 13.5,23 9,20 4.5,23 6,18 2,15 7,15"/><polygon points="17,3 18,5.5 20.5,5.5 18.5,7 19.3,9.5 17,8 14.7,9.5 15.5,7 13.5,5.5 16,5.5"/><circle cx="21" cy="17" r="1.3"/></svg>
  </section>

  <section class="step" style="left:359px">
    <svg class="step-badge" viewBox="0 0 60 60"><circle cx="30" cy="30" r="27" fill="none" stroke="var(--teal)" stroke-width="4"/><circle cx="30" cy="30" r="21" fill="var(--teal)"/><text x="30" y="37" text-anchor="middle" font-family="Tinos, serif" font-size="20" fill="#fff">2</text></svg>
    <h2 class="step-title">PERSONAL COLLECTION</h2>
    <p class="step-text">We choose the pieces we know<br>the velloire customer will love</p>
    <svg class="step-icon" viewBox="0 0 26 26" fill="var(--teal)"><path d="M13 23 C6 16 4 13 4 9.5 C4 6.5 6.3 4.5 8.8 4.5 C10.7 4.5 12.2 5.6 13 7 C13.8 5.6 15.3 4.5 17.2 4.5 C19.7 4.5 22 6.5 22 9.5 C22 13 20 16 13 23 Z"/></svg>
  </section>

  <section class="step" style="left:593px">
    <svg class="step-badge" viewBox="0 0 60 60"><circle cx="30" cy="30" r="27" fill="none" stroke="var(--teal)" stroke-width="4"/><circle cx="30" cy="30" r="21" fill="var(--teal)"/><text x="30" y="37" text-anchor="middle" font-family="Tinos, serif" font-size="20" fill="#fff">3</text></svg>
    <h2 class="step-title">WE PREPARE</h2>
    <p class="step-text">Brandsparkling or nearly new.</p>
    <svg class="step-icon" viewBox="0 0 26 26"><circle cx="13" cy="13" r="11" fill="var(--teal)"/></svg>
  </section>

  <section class="step" style="left:824px">
    <svg class="step-badge" viewBox="0 0 60 60"><circle cx="30" cy="30" r="27" fill="none" stroke="var(--teal)" stroke-width="4"/><circle cx="30" cy="30" r="21" fill="var(--teal)"/><text x="30" y="37" text-anchor="middle" font-family="Tinos, serif" font-size="20" fill="#fff">4</text></svg>
    <h2 class="step-title">ONCE SOLD</h2>
    <p class="step-text">Brandsparkling or nearly new.</p>
    <svg class="step-icon" viewBox="0 0 26 26" fill="var(--teal)"><g transform="rotate(-45 13 13)"><path d="M13 1 C14.3 1 15 2.3 15 4 V10 L24 15 V17.5 L15 14.5 V20 L18 22.5 V24.5 L13 23 L8 24.5 V22.5 L11 20 V14.5 L2 17.5 V15 L11 10 V4 C11 2.3 11.7 1 13 1 Z"/></g></svg>
  </section>

  <section class="step" style="left:1063px">
    <svg class="step-badge" viewBox="0 0 60 60"><circle cx="30" cy="30" r="27" fill="none" stroke="var(--teal)" stroke-width="4"/><circle cx="30" cy="30" r="21" fill="var(--teal)"/><text x="30" y="37" text-anchor="middle" font-family="Tinos, serif" font-size="20" fill="#fff">5</text></svg>
    <h2 class="step-title">YOUR PAYMENT</h2>
  </section>

  <div class="payment-options">
    <div class="payment-option">
      <p>Pocket<br>your cash</p>
      <p class="currency">$€£</p>
    </div>
    <div class="payment-divider"></div>
    <div class="payment-option">
      <p>Donate your<br>cash to charity</p>
      <svg class="halo-icon" viewBox="0 0 26 30"><ellipse cx="13" cy="4" rx="6" ry="2" fill="none" stroke="var(--teal)" stroke-width="1.4"/><circle cx="13" cy="18" r="10.5" fill="var(--teal)"/></svg>
    </div>
  </div>

  <footer class="action-band">
    <a class="cta" href="#">GET STARTED <svg viewBox="0 0 8 10"><polygon points="0,0 8,5 0,10" fill="#fff"/></svg></a>
  </footer>
</body>
</html>
```